Business Cards for a law firm

Business cards for our law firm. Use our silhoette logo and OAK HARBOR - check our website (www.oakharbor-legal.com)

Contact Information for Business Card

our silhouette logo, OAK HARBOR, 800-555-0147, Dorian Kestrup, dorian@oakharbor-legal.com

Requirements
Must have
• our silhouette logo, OAK HARBOR, 800-555-0147, Dorian Kestrup, dorian@oakharbor-legal.com

```html
<!DOCTYPE html>
<html lang="en">
<head>
<meta charset="utf-8">
<title>Oak Harbor — Business Cards</title>
<link rel="stylesheet" href="https://fonts.googleapis.com/css2?family=Cinzel:wght@600;700&family=Arimo:wght@400;700&display=swap">
<style>
  :root {
    --navy: #1a2f6a;
    --paper: #f4f4f5;
    --backdrop: #dadada;
    --ink: #222428;
    --rule-grey: #55585e;
    --white: #ffffff;
  }
  * { margin: 0; padding: 0; box-sizing: border-box; }
  html, body { width: 1200px; height: 1040px; overflow: hidden; }
  body { background: var(--backdrop); position: relative; font-family: "Arimo", Arial, sans-serif; }

  .card {
    position: absolute;
    left: 284px;
    width: 644px;
    height: 368px;
    border-radius: 16px;
    overflow: hidden;
  }
  .card--front { top: 130px; background: var(--paper); }
  .card--back { top: 567px; background: var(--navy); }

  .brand {
    position: absolute;
    left: 62px;
    top: 164px;
    display: flex;
    align-items: center;
    gap: 12px;
  }
  .brand__mark { width: 30px; height: 30px; background: var(--navy); }
  .brand__name {
    font-family: "Cinzel", Georgia, serif;
    font-weight: 700;
    font-size: 21px;
    letter-spacing: 1.5px;
    color: var(--navy);
  }

  .divider {
    position: absolute;
    left: 325px;
    top: 124px;
    width: 1px;
    height: 118px;
    background: #9a9ca2;
  }

  .person-name {
    position: absolute;
    left: 345px;
    top: 122px;
    font-family: "Cinzel", Georgia, serif;
    font-weight: 700;
    font-size: 22px;
    letter-spacing: 0.5px;
    color: var(--navy);
  }

  .contacts {
    position: absolute;
    left: 345px;
    top: 176px;
    list-style: none;
  }
  .contacts li {
    display: flex;
    align-items: center;
    gap: 9px;
    height: 20.5px;
    font-size: 15.5px;
    color: var(--ink);
  }
  .contacts svg { width: 12px; height: 12px; fill: var(--navy); flex: none; }

  .front-rule {
    position: absolute;
    left: 0; right: 0;
    top: 344px;
    height: 3px;
    background: var(--rule-grey);
  }
  .front-band {
    position: absolute;
    left: 0; right: 0;
    top: 350px;
    bottom: 0;
    background: var(--navy);
  }

  .back-name {
    position: absolute;
    left: 0; right: 0;
    top: 150px;
    text-align: center;
    font-family: "Cinzel", Georgia, serif;
    font-weight: 700;
    font-size: 40px;
    letter-spacing: 4px;
    color: var(--white);
  }
  .back-url {
    position: absolute;
    left: 0; right: 0;
    top: 323px;
    text-align: center;
    font-weight: 700;
    font-size: 13px;
    letter-spacing: 4px;
    color: var(--white);
  }
</style>
</head>
<body>
  <section class="card card--front">
    <div class="brand">
      <span class="brand__mark"></span>
      <span class="brand__name">OAK HARBOR</span>
    </div>
    <div class="divider"></div>
    <h1 class="person-name">Dorian Kestrup</h1>
    <ul class="contacts">
      <li>
        <svg viewBox="0 0 24 24"><path d="M6.6 10.8a15 15 0 0 0 6.6 6.6l2.2-2.2a1 1 0 0 1 1-.25 11.4 11.4 0 0 0 3.6.57 1 1 0 0 1 1 1V20a1 1 0 0 1-1 1A17 17 0 0 1 3 4a1 1 0 0 1 1-1h3.5a1 1 0 0 1 1 1c0 1.25.2 2.45.57 3.57a1 1 0 0 1-.25 1z"/></svg>
        800-555-0147
      </li>
      <li>
        <svg viewBox="0 0 24 24"><path d="M2 5h20v14H2z M3.5 6.5 12 13l8.5-6.5" stroke="#f4f4f5" stroke-width="1.6"/></svg>
        dorian@oakharbor-legal.com
      </li>
      <li>
        <svg viewBox="0 0 24 24"><circle cx="12" cy="12" r="10"/><path d="M8 6c2 1 1 3 3 4s1 3-1 4M15 15c1-1 3-1 4 0" stroke="#f4f4f5" stroke-width="1.6" fill="none"/></svg>
        www.oakharbor-legal.com
      </li>
    </ul>
    <div class="front-rule"></div>
    <div class="front-band"></div>
  </section>

  <section class="card card--back">
    <p class="back-name">OAK HARBOR</p>
    <p class="back-url">WWW.OAKHARBOR-LEGAL.COM</p>
  </section>
</body>
</html>
```